Suds Harbor Laundromat Wordpress Design

We need a Wordpress website design for our laundromat, Suds Harbor Atlanta, at www.sudsharboratlanta-example.com. We would like to have 6 pages: Home, About Us, Services, Locations, Reviews and Contact us. We will provide content for the text on each page. What we do: We are a full service laundromat that provides dry cleaning drop off, professional laundry services, wash dry fold and self service laundry to the local community. We would like to use the color scheme from our logo to convey a warm, safe, and bright business that caters to its diverse community.
Updates

I like the structure of this laundromat website: http://www.tumblewashhub-example.com/ Using my logo and color scheme in the above referenced website is what. Am looking for. The photos attached to the project with the female model should be used as a primary focus and supplemented by actual photos of the equipment.

Target Market(s)

Our target market is a diverse group of people from Midtown Atlanta - LGBTQ community /Locals/Regulars that have been coming to laundromat for 30 years.

Industry/Entity Type

Laundromat

Coding

Coded - Design and coding required

Number of Pages Required

5+ page

Font styles to use
Sans Serif

Colors
0054AA
0677BA
7BADD7
CADEEF
E8F1F8

Requirements
Must have
• Feature this video on the main page: https://video.example.com/Qx7mBr2Lp0Z

```html
<!DOCTYPE html>
<html lang="en">
<head>
<meta charset="utf-8">
<title>Suds Harbor Laundromat</title>
<link href="https://fonts.googleapis.com/css2?family=Oswald:wght@500;600&family=Poppins:wght@400;500;600&display=swap" rel="stylesheet">
<style>
:root{
  --blue-deep:#0054AA;
  --blue:#0677BA;
  --blue-mid:#7BADD7;
  --blue-pale:#CADEEF;
  --blue-mist:#E8F1F8;
  --navy:#0b3f86;
  --heading:#0a5aa8;
  --text:#333;
  --white:#fff;
}
*{margin:0;padding:0;box-sizing:border-box}
html,body{width:1200px;height:4189px;overflow:hidden}
body{position:relative;background:var(--white);font-family:'Poppins',sans-serif;color:var(--text)}
.abs{position:absolute}
.display{font-family:'Oswald',sans-serif;font-weight:500;text-transform:uppercase;letter-spacing:-.5px}

/* header */
.site-nav{left:89px;top:13px;width:1022px;height:68px;background:var(--white);border-radius:34px;box-shadow:0 6px 20px rgba(0,0,0,.15);display:flex;align-items:center;padding:0 48px 0 32px}
.brand{font-family:'Oswald',sans-serif;font-weight:500;font-size:28px;color:var(--blue-deep);text-transform:uppercase;display:flex;align-items:center;gap:10px}
.brand-dot{width:14px;height:14px;border-radius:50%;background:var(--blue)}
.menu{margin-left:auto;display:flex;gap:24px;align-items:center;list-style:none}
.menu li{font-family:'Oswald',sans-serif;font-size:19px;color:var(--blue-deep);text-transform:uppercase}

/* hero */
.hero-photo{left:0;top:0;width:1200px;height:800px;background:linear-gradient(120deg,#5d6a70 0%,#b7c0c2 35%,#d9dcd8 55%,#8d979a 80%,#4f5b60 100%)}
.hero-title{left:85px;top:336px;font-size:56px;line-height:54px;color:var(--white);text-shadow:0 2px 8px rgba(0,0,0,.35)}

/* services */
.section-title{left:0;width:1200px;text-align:center;color:var(--heading);font-size:40px}
.service-photo{border-radius:50%;box-shadow:0 18px 40px rgba(0,0,0,.18)}
.service-ring{border-radius:50%;border:5px solid var(--blue-deep);border-right-color:transparent;border-bottom-color:transparent}
.service-heading{color:var(--heading);font-size:41px;line-height:1}
.service-text{width:390px;font-size:14.5px;line-height:22.5px;color:#333}
.btn-outline{display:inline-block;border:3px solid var(--blue);border-radius:20px;font-size:13px;font-weight:600;color:var(--blue-deep);text-transform:uppercase;text-align:center;line-height:27px;width:147px;letter-spacing:.5px}
.drop{border-radius:50%;background:var(--blue-deep)}

/* laundromat band */
.band-kicker{left:0;width:1200px;text-align:center;color:var(--white);font-size:27px}
.band-title{left:0;width:1200px;text-align:center;color:var(--white);font-size:41px;line-height:44px}
.band-text{left:215px;width:770px;text-align:center;color:var(--white);font-size:16px;line-height:25px}
.btn-ghost{left:488px;top:2478px;width:223px;height:41px;border:2px solid rgba(255,255,255,.8);border-radius:21px;color:var(--white);font-size:14px;font-weight:600;text-align:center;line-height:37px;letter-spacing:.5px}
.video-frame{left:239px;top:2572px;width:724px;height:423px;border-radius:10px;background:linear-gradient(135deg,#a9a79b 0%,#8b8a83 40%,#6f7276 100%);box-shadow:0 30px 60px rgba(0,0,0,.25)}
.play-btn{left:568px;top:2754px;width:64px;height:64px;border-radius:50%;background:#d40f14;display:flex;align-items:center;justify-content:center}

/* testimonials */
.quote-mark{left:82px;top:3190px;font-family:'Oswald',sans-serif;font-size:130px;line-height:1;color:#d6d6d6}
.testi-heading{left:85px;top:3280px;color:var(--heading);font-size:41px;line-height:45px}
.testi-text{left:85px;top:3374px;width:490px;font-size:14.5px;line-height:22.5px}
.testi-name{left:85px;top:3468px;font-size:15px;font-weight:600;color:var(--blue-deep);text-transform:uppercase}
.testi-place{left:85px;top:3490px;font-size:11px}
.avatar{border-radius:50%;background:linear-gradient(145deg,#c6ab95,#6d5548);box-shadow:0 6px 14px rgba(0,0,0,.25);border:3px solid var(--white)}

/* footer */
.footer-brand{left:89px;top:3920px;font-family:'Oswald',sans-serif;font-size:44px;font-weight:500;color:var(--white);text-transform:uppercase;display:flex;align-items:center;gap:12px}
.footer-col{top:3898px;color:var(--white)}
.footer-col h3{font-family:'Oswald',sans-serif;font-weight:500;font-size:22px;text-transform:uppercase}
.footer-col h3::after{content:"";display:block;width:32px;height:3px;background:var(--blue-mid);margin:6px 0 12px}
.footer-col p,.footer-col li{font-size:13px;line-height:23px;list-style:none}
.social{display:flex;gap:14px;margin-top:6px}
.social span{width:10px;height:10px;border-radius:50%;background:var(--white)}
.footer-rule{left:89px;top:4143px;width:1022px;height:1px;background:rgba(255,255,255,.25)}
.copyright{left:89px;top:4156px;font-size:12px;color:var(--white)}
.to-top{left:1130px;top:4102px;width:40px;height:40px;border-radius:50%;background:var(--blue);display:flex;align-items:center;justify-content:center}
.badge{left:1066px;top:4155px;width:42px;height:22px;border-radius:11px;background:var(--white)}
</style>
</head>
<body>

<!-- HERO -->
<div class="abs hero-photo" role="img" aria-label="Photo of a woman in a blue dress walking past rows of front-loading washers in the laundromat"></div>
<svg class="abs" style="left:0;top:640px" width="1200" height="180" viewBox="0 0 1200 180">
  <path d="M0 60 C200 190 420 130 620 70 C820 10 1000 20 1200 160 L1200 180 L0 180Z" fill="#fff"/>
  <path d="M0 60 C200 190 420 130 620 70 C700 48 780 38 840 38" fill="none" stroke="#0054AA" stroke-width="9"/>
</svg>

<nav class="abs site-nav">
  <div class="brand"><span class="brand-dot"></span>Suds Harbor</div>
  <ul class="menu">
    <li><svg width="18" height="16" viewBox="0 0 18 16"><path d="M9 0L0 8h3v8h4v-5h4v5h4V8h3z" fill="#0054AA"/></svg></li>
    <li>About Us</li><li>Services</li><li>Locations</li><li>Reviews</li><li>Contact Us</li>
  </ul>
</nav>

<h1 class="abs display hero-title">Coin Laundry, Dry<br>Cleaning, &amp; Professional<br>Laundry</h1>

<!-- SERVICES -->
<h2 class="abs display section-title" style="top:880px">Our Services</h2>

<div class="abs drop" style="left:364px;top:904px;width:26px;height:26px"></div>
<div class="abs drop" style="left:305px;top:938px;width:15px;height:15px"></div>
<div class="abs drop" style="left:421px;top:936px;width:15px;height:15px"></div>
<div class="abs service-photo" style="left:154px;top:959px;width:358px;height:358px;background:linear-gradient(135deg,#9aa6ab,#d4d8d6 60%,#7d878b)" role="img" aria-label="Photo of a row of stainless washers in the laundromat"></div>
<div class="abs service-ring" style="left:149px;top:954px;width:368px;height:368px;transform:rotate(-30deg)"></div>
<h3 class="abs display service-heading" style="left:593px;top:1032px">Coin Laundry</h3>
<p class="abs service-text" style="left:593px;top:1085px">Lorem Ipsum is simply dummy text of the printing and typesetting industry. Lorem Ipsum has been the industry's standard dummy text ever since the 1500s, when an unknown printer took a galley .</p>
<span class="abs btn-outline" style="left:593px;top:1191px">Learn More</span>

<div class="abs drop" style="left:1031px;top:1300px;width:22px;height:22px"></div>
<div class="abs drop" style="left:967px;top:1280px;width:14px;height:14px"></div>
<div class="abs drop" style="left:1051px;top:1360px;width:14px;height:14px"></div>
<div class="abs service-photo" style="left:652px;top:1288px;width:358px;height:358px;background:linear-gradient(135deg,#cfd3d0,#8f999c 50%,#3f6fb2)" role="img" aria-label="Photo of a woman in a blue dress with a laundry cart beside the washers"></div>
<h3 class="abs display service-heading" style="left:193px;top:1396px">Dry Cleaning</h3>
<p class="abs service-text" style="left:193px;top:1449px">Lorem Ipsum is simply dummy text of the printing and typesetting industry. Lorem Ipsum has been the industry's standard dummy text ever since the 1500s, when an unknown printer took a galley .</p>
<span class="abs btn-outline" style="left:193px;top:1555px">Learn More</span>

<div class="abs drop" style="left:364px;top:1614px;width:26px;height:26px"></div>
<div class="abs drop" style="left:305px;top:1672px;width:15px;height:15px"></div>
<div class="abs drop" style="left:421px;top:1644px;width:15px;height:15px"></div>
<div class="abs service-photo" style="left:154px;top:1671px;width:358px;height:358px;background:linear-gradient(180deg,#a7bcb6,#c9cdc7 45%,#8c9394)" role="img" aria-label="Photo of the laundromat wall sign above a row of washers"></div>
<div class="abs service-ring" style="left:149px;top:1666px;width:368px;height:368px;transform:rotate(-30deg)"></div>
<h3 class="abs display service-heading" style="left:593px;top:1750px">Professional Laundry</h3>
<p class="abs service-text" style="left:593px;top:1803px">Lorem Ipsum is simply dummy text of the printing and typesetting industry. Lorem Ipsum has been the industry's standard dummy text ever since the 1500s, when an unknown printer took a galley .</p>
<span class="abs btn-outline" style="left:593px;top:1908px">Learn More</span>

<!-- LAUNDROMAT BAND -->
<svg class="abs" style="left:0;top:2040px" width="1200" height="880" viewBox="0 0 1200 880">
  <defs><linearGradient id="bandFill" x1="0" y1="0" x2="0" y2="1"><stop offset="0" stop-color="#0677BA"/><stop offset="1" stop-color="#0a63b0"/></linearGradient></defs>
  <path d="M0 40 C180 110 380 120 580 60 C780 0 1000 -10 1200 120 L1200 780 C1050 680 900 740 700 800 C450 870 200 840 0 740Z" fill="url(#bandFill)"/>
  <path d="M963 798 C1060 760 1140 770 1200 830 L1200 850 C1140 790 1060 780 963 815Z" fill="#1190e0"/>
</svg>
<p class="abs display band-kicker" style="top:2252px">Laundromat Services</p>
<h2 class="abs display band-title" style="top:2290px">Quality Self Service Coin Operated<br>Washers and Dryers</h2>
<p class="abs band-text" style="top:2385px">Lorem Ipsum is simply dummy text of the printing and typesetting industry. Lorem Ipsum has been the industry's standard dummy text ever since the 1500s, when an unknown printer took a galley of type and scrambled it to make a type specimen book.</p>
<span class="abs btn-ghost">LEARN MORE ABOUT US</span>

<div class="abs video-frame" role="img" aria-label="Featured laundromat video still: a woman with headphones inside Suds Harbor Atlanta"></div>
<div class="abs play-btn"><svg width="22" height="24" viewBox="0 0 22 24"><path d="M2 1l19 11L2 23z" fill="#fff"/></svg></div>

<!-- TESTIMONIALS -->
<div class="abs quote-mark">&ldquo;</div>
<h2 class="abs display testi-heading">Our Customers Love<br>Our Services</h2>
<p class="abs testi-text">Lorem Ipsum is simply dummy text of the printing and typesetting industry. Lorem Ipsum has been the industry's standard dummy text ever since the 1500s, when an unknown printer took a galley of type and scrambled it to make a type specimen .</p>
<p class="abs testi-name">Jordan Ellis</p>
<p class="abs testi-place">Atlanta Ga</p>

<svg class="abs" style="left:660px;top:3060px" width="540" height="580" viewBox="0 0 540 580">
  <circle cx="272" cy="286" r="274" fill="none" stroke="#e6e6e6" stroke-width="2"/>
  <circle cx="272" cy="286" r="73" fill="none" stroke="#e6e6e6" stroke-width="2"/>
</svg>
<div class="abs avatar" style="left:691px;top:3192px;width:162px;height:162px" role="img" aria-label="Customer portrait"></div>
<div class="abs avatar" style="left:1044px;top:3321px;width:100px;height:100px" role="img" aria-label="Customer portrait"></div>
<div class="abs avatar" style="left:881px;top:3398px;width:124px;height:124px" role="img" aria-label="Customer portrait"></div>
<div class="abs avatar" style="left:913px;top:3244px;width:54px;height:54px" role="img" aria-label="Customer portrait"></div>
<div class="abs avatar" style="left:760px;top:3390px;width:66px;height:66px" role="img" aria-label="Customer portrait"></div>
<div class="abs avatar" style="left:753px;top:3077px;width:42px;height:42px" role="img" aria-label="Customer portrait"></div>
<div class="abs avatar" style="left:997px;top:3125px;width:36px;height:36px" role="img" aria-label="Customer portrait"></div>
<div class="abs avatar" style="left:734px;top:3506px;width:38px;height:38px" role="img" aria-label="Customer portrait"></div>
<div class="abs avatar" style="left:1004px;top:3550px;width:60px;height:60px" role="img" aria-label="Customer portrait"></div>

<!-- FOOTER -->
<svg class="abs" style="left:0;top:3630px" width="1200" height="559" viewBox="0 0 1200 559">
  <path d="M0 120 C200 60 380 20 560 90 C740 160 900 40 1200 0 L1200 559 L0 559Z" fill="#0a4f9c"/>
  <path d="M0 170 C220 110 400 80 600 150 C800 210 980 110 1200 80 L1200 559 L0 559Z" fill="#0b3f86"/>
</svg>
<div class="abs footer-brand"><span class="brand-dot" style="background:#7BADD7"></span>Suds Harbor</div>

<div class="abs footer-col" style="left:439px">
  <h3>Useful Links</h3>
  <ul><li>Home</li><li>About Us</li><li>Services</li><li>Locations</li><li>Reviews</li><li>Contact us</li></ul>
</div>
<div class="abs footer-col" style="left:646px">
  <h3>Hours</h3>
  <p>Covid 19 Hours -<br>Open 7 days a week<br>8 am to 8 pm last wash<br>begins 6:30 pm</p>
</div>
<div class="abs footer-col" style="left:842px">
  <h3>Contact Us</h3>
  <p>Suds Harbor Atlanta -<br>Birchwood Commons Center, 2210<br>Larkspur Ave NE, # 118, Atlanta, GA 30399<br>(404) 555-0142</p>
  <div class="social"><span></span><span></span></div>
</div>

<div class="abs footer-rule"></div>
<p class="abs copyright">&copy;Copyright 2021 | All Rights Reserved</p>
<div class="abs badge"></div>
<div class="abs to-top"><svg width="12" height="8" viewBox="0 0 12 8"><path d="M1 7l5-5 5 5" fill="none" stroke="#fff" stroke-width="2"/></svg></div>

</body>
</html>
```